Veltara Structural Approval Standards Private Assessors

Professional Construction Consultancy Company Business Card - must keep logo colours see images below - examples have been added from my last competition - please see them as examples only!

Target Market(s)

Home Builders

Industry/Entity Type

Construction

Contact Information for Business Card

See "must haves"

Font styles to use
Sans Serif

Colors
ffffff
add136
000000

Requirements
Must have
• Daniel Moravi
• Director
• Phone: 0431 587 219
• Address: 7 Tarrunga Rd,
• Hallworth Vale, SA, 5091
• Email: veltaraassessors@mailbox-example.com
• Website: www.veltaraassessors-example.com.au
• Facebook: Veltara Structural Approval Standards
Nice to have
• Side 1: full logo
• Side 2: company details
Should not have
• hard to read
• must be clear and professional

```html
<!DOCTYPE html>
<html lang="en">
<head>
<meta charset="utf-8">
<title>Veltara Structural Approval Standards – Business Card</title>
<link rel="stylesheet" href="https://fonts.googleapis.com/css2?family=Open+Sans:wght@400;600;700&display=swap">
<style>
  :root {
    --green: #add136;
    --black: #000000;
    --white: #ffffff;
    --ink: #1a1a1a;
    --stage: #e9e7e4;
  }
  * { box-sizing: border-box; margin: 0; padding: 0; }
  html, body {
    width: 1200px; height: 716px; overflow: hidden;
    background: var(--stage);
    font-family: "Open Sans", Arial, sans-serif;
  }
  .sheet {
    width: 1200px; height: 716px;
    display: flex; align-items: center; justify-content: center; gap: 50px;
  }
  .card {
    width: 520px; height: 300px; border-radius: 12px;
    position: relative; overflow: hidden;
    box-shadow: 0 6px 18px rgba(0,0,0,.18);
  }
  /* Side 1 */
  .card--front { background: var(--black); display: flex; align-items: center; justify-content: center; }
  .brand { display: flex; align-items: center; gap: 14px; }
  .brand__mark { width: 18px; height: 18px; flex: none; }
  .brand__name {
    font-weight: 700; line-height: 1.2; text-transform: uppercase; letter-spacing: .06em;
  }
  .card--front .brand__mark { background: var(--green); }
  .card--front .brand__name { color: var(--green); font-size: 21px; }
  /* Side 2 */
  .card--back { background: var(--white); }
  .card--back .brand { position: absolute; left: 36px; top: 60px; gap: 10px; }
  .card--back .brand__mark { width: 12px; height: 12px; background: var(--black); }
  .card--back .brand__name { color: var(--green); font-size: 11.5px; letter-spacing: .05em; }
  .swoosh { position: absolute; inset: 0; width: 100%; height: 100%; }
  .contact { position: absolute; left: 300px; top: 84px; color: var(--ink); }
  .contact__name { font-size: 17px; font-weight: 600; line-height: 1.1; }
  .contact__role { font-size: 12px; color: var(--green); margin-bottom: 10px; }
  .contact__list { list-style: none; font-size: 11px; line-height: 1.35; }
  .contact__list li { display: flex; gap: 8px; align-items: flex-start; margin-bottom: 3px; }
  .icon { width: 10px; height: 10px; flex: none; margin-top: 3px; fill: var(--green); }
</style>
</head>
<body>
<main class="sheet">
  <section class="card card--front" aria-label="Business card front">
    <div class="brand">
      <span class="brand__mark"></span>
      <p class="brand__name">Veltara Structural<br>Approval Standards<br>Private Assessors</p>
    </div>
  </section>

  <section class="card card--back" aria-label="Business card back">
    <svg class="swoosh" viewBox="0 0 520 300" preserveAspectRatio="none" aria-hidden="true">
      <path fill="var(--black)" d="M0,150 C50,180 150,218 330,252 C200,242 70,222 0,196 Z"/>
      <path fill="var(--green)" d="M0,206 C80,252 250,272 390,268 C450,266 495,255 520,244 L520,300 L0,300 Z"/>
    </svg>

    <div class="brand">
      <span class="brand__mark"></span>
      <p class="brand__name">Veltara Structural<br>Approval Standards<br>Private Assessors</p>
    </div>

    <div class="contact">
      <p class="contact__name">Daniel Moravi</p>
      <p class="contact__role">Director</p>
      <ul class="contact__list">
        <li><svg class="icon" viewBox="0 0 10 10"><path d="M2 0 L4 2.5 L3 3.6 C3.6 5 5 6.4 6.4 7 L7.5 6 L10 8 L8.6 10 C4 9.6 0.4 6 0 1.4 Z"/></svg><span>0431 587 219</span></li>
        <li><svg class="icon" viewBox="0 0 10 10"><path d="M5 0 C2.8 0 1.3 1.6 1.3 3.6 C1.3 6 5 10 5 10 C5 10 8.7 6 8.7 3.6 C8.7 1.6 7.2 0 5 0 Z M5 2.3 A1.3 1.3 0 1 1 5 4.9 A1.3 1.3 0 1 1 5 2.3 Z"/></svg><span>7 Tarrunga Rd,<br>Hallworth Vale, SA, 5091</span></li>
        <li><svg class="icon" viewBox="0 0 10 10"><path d="M0 2 H10 V8 H0 Z M0.6 2.4 L5 5.6 L9.4 2.4 V2.9 L5 6.2 L0.6 2.9 Z" fill-rule="evenodd"/></svg><span>veltaraassessors@mailbox-example.com</span></li>
        <li><svg class="icon" viewBox="0 0 10 10"><circle cx="5" cy="5" r="4.4" fill="none" stroke="var(--green)" stroke-width="1"/><ellipse cx="5" cy="5" rx="1.8" ry="4.4" fill="none" stroke="var(--green)" stroke-width=".8"/><path d="M0.6 5 H9.4" stroke="var(--green)" stroke-width=".8"/></svg><span>www.veltaraassessors-example.com.au</span></li>
        <li><svg class="icon" viewBox="0 0 10 10"><rect x="0.5" y="0.5" width="9" height="9" rx="1.5"/></svg><span>Veltara Structural Approval Standards</span></li>
      </ul>
    </div>
  </section>
</main>
</body>
</html>
```